4Star Hotel looking for web design

Hello everyone,
We are located in Cambodia, the hotel should open in 2-3 months. The name will be Velmora-Boutique Hotel. We are looking for a webdesign which is professional, elegant and SIMPLE.
All informations should be easy to find. We are quite open to proposition but we would like to the home page:
-a carousel with around 5-8 picture
-Little menu where we can book a room
By the way, we would like a page for our restaurant, gallery, contact page for description of the rooms. I add some old pictures.
I give an example of what we are expecting:
www.quenrostays.com/tovelspring
We hope that we are proposing a good job for you guys. Have fun and Thanks.
Oh and the winner ( or someone he had choose) of course have free night in our presidential suite
Target Market(s)
We are looking for european Market. Let s say people middle age who are willing to travel in difficult area
Industry/Entity Type
Hotel
Coding
Coded - Design and coding required
Number of Pages Required
5+ page
Requirements
Must have
- Simple, simple and Simple
- Carousel
- place for book a room
- during booking, a menu for select room , and after that another menu for propose like tour in town, taxi, flower, bottle of champagne for example
- during all the process, the customer should be able to know at what step it is and can stop and come back after
- Have to be perfect for smartphone
- Price with drawbar for they know how much they earn with our reduction
Nice to have
- during the process of information (name, adress, tel...), it would be great if they can fill it with a button facebook, google plus, lindkdin, instagram ....
- then a button share on facebook, twitter for know that they book in our hotel
- At the end of the booking, a flashcode with the recapitulatif that customer can scan.

```html
<!DOCTYPE html>
<html lang="en">
<head>
<meta charset="utf-8">
<title>Velmora Boutique Hotel</title>
<link href="https://fonts.googleapis.com/css2?family=Open+Sans:wght@400;600;700&display=swap" rel="stylesheet">
<style>
:root{
  --maroon:#4b1c1c;
  --maroon-dark:#3a1414;
  --orange:#f39a1e;
  --orange-dark:#e07f0c;
  --btn:#5b1f1f;
  --text:#444;
  --muted:#777;
  --light:#eeeeee;
  --white:#fff;
}
*{box-sizing:border-box;margin:0;padding:0}
html,body{width:747px;height:1200px;overflow:hidden}
body{font-family:"Open Sans",Arial,sans-serif;color:var(--text);background:var(--white);font-size:6px;line-height:1.45}
.wrap{width:560px;margin:0 auto;position:relative}
/* header */
.topbar{background:var(--maroon);height:70px;color:var(--white)}
.topbar .wrap{display:flex;align-items:center;height:70px;justify-content:space-between}
.brand{display:flex;align-items:center;gap:6px}
.brand-mark{width:14px;height:14px;background:var(--orange)}
.brand-name{font-size:12px;font-weight:600;line-height:1.1;color:var(--white)}
.local{text-align:center;font-size:6.5px}
.local b{display:block;font-size:7px;font-weight:600;margin-bottom:2px}
.live-chat{background:var(--orange);color:var(--white);font-size:9px;font-weight:700;padding:6px 10px;border-radius:2px}
.contact-top{text-align:right;font-size:7px}
.social{display:flex;gap:3px;justify-content:flex-end;align-items:center;margin-bottom:4px}
.social span{width:9px;height:9px;border-radius:50%;background:var(--orange);display:inline-block}
.phone{font-size:10px;font-weight:600;display:flex;align-items:center;gap:4px;justify-content:flex-end}
/* nav */
.nav{background:var(--orange);height:20px}
.nav ul{list-style:none;display:flex;height:20px;align-items:center}
.nav li{font-size:6.5px;font-weight:600;color:var(--white);padding:0 9px;height:20px;line-height:20px;border-right:1px solid rgba(255,255,255,.35)}
.nav li.active{background:var(--maroon)}
/* carousel */
.carousel{height:160px;background:#2a2a2a;position:relative;display:flex;gap:2px;padding:0 93px}
.slide{flex:1}
.s1{background:linear-gradient(160deg,#b9a88f,#6b5a47)}
.s2{background:linear-gradient(160deg,#8d6d55,#3e2c22)}
.s3{background:linear-gradient(160deg,#d8d0c4,#7c6a58)}
.s4{background:linear-gradient(160deg,#a88d74,#4d3a2d)}
.arrow{position:absolute;top:68px;width:20px;height:24px;display:flex;align-items:center;justify-content:center}
.arrow.l{left:100px}.arrow.r{right:100px}
/* booking */
.booking{background:var(--orange);height:55px}
.booking .wrap{display:flex;align-items:center;gap:5px;height:55px}
.field{display:flex;flex-direction:column;gap:2px;color:var(--white);font-size:5.5px;font-weight:600}
.field .box{background:var(--white);width:62px;height:12px;border-radius:1px;color:var(--muted);font-weight:400;padding:2px 3px;display:flex;justify-content:space-between;align-items:center}
.field.small .box{width:44px}
.check{display:flex;align-items:center;gap:3px;margin-left:auto}
.check .dot{width:18px;height:18px;border-radius:50%;background:var(--white);display:flex;align-items:center;justify-content:center}
.check .btn{background:var(--btn);color:var(--white);font-size:6px;font-weight:700;padding:4px 7px}
/* welcome */
.welcome{text-align:center;padding:16px 0 18px}
h2{font-size:13px;font-weight:400;color:#333;margin-bottom:6px}
.welcome p{width:470px;margin:0 auto 8px;font-size:5.5px;color:var(--muted);text-align:left}
.btn-read{display:inline-block;background:var(--btn);color:var(--white);font-size:5.5px;font-weight:700;padding:4px 9px}
.divider{height:1px;background:#ddd}
/* facilities */
.facilities{text-align:center;padding:20px 0 22px;height:225px}
.fac-grid{display:flex;justify-content:space-between;margin-top:14px}
.fac{width:125px}
.fac svg{display:block;margin:0 auto 6px}
.fac h3{font-size:6.5px;font-weight:700;color:#333;margin-bottom:4px}
.fac p{font-size:5px;color:var(--muted);margin-bottom:6px}
.fac .btn-read{font-size:5px;padding:3px 7px}
/* offers */
.offers{background:var(--light);height:212px;padding-top:10px;text-align:center}
.offer-row{display:flex;gap:10px;margin-top:8px;justify-content:center}
.offer-img{width:160px;height:145px}
.o1{background:linear-gradient(135deg,#f3c23a,#e0452b)}
.o2{background:linear-gradient(135deg,#d81e2c,#8e0d16)}
.offer-info{width:200px;background:var(--white);padding:14px 14px;text-align:left}
.offer-info .pct{color:var(--orange-dark);font-size:9px;font-weight:700}
.offer-info .title{font-size:7.5px;color:#333;font-weight:600}
.offer-info .price{font-size:6px;color:#c0392b;margin-bottom:6px}
.offer-info p{font-size:5.5px;color:var(--muted);margin-bottom:3px}
.offer-info .details{display:block;background:var(--btn);color:var(--white);text-align:center;font-size:6px;font-weight:700;padding:5px;margin-top:8px}
/* gallery */
.gallery{height:150px;text-align:center;padding-top:10px}
.gal-row{display:flex;gap:3px;justify-content:center;align-items:center;margin-top:8px}
.gal-row .g{width:105px;height:72px}
.g1{background:linear-gradient(150deg,#c8b9a3,#6f5c49)}
.g2{background:linear-gradient(150deg,#9e7c61,#4a3426)}
.g3{background:linear-gradient(150deg,#b8a58e,#5b4736)}
.g4{background:linear-gradient(150deg,#d7cbbb,#8a7560)}
.g5{background:linear-gradient(150deg,#8c7460,#3c2b20)}
/* footer */
.footer{background:var(--maroon);height:160px;color:#e6d9d9}
.footer .wrap{display:flex;gap:18px;padding-top:16px}
.footer h4{font-size:7px;font-weight:700;color:var(--white);margin-bottom:6px}
.links{display:grid;grid-template-columns:60px 60px;gap:2px 6px;font-size:5.5px}
.contact-info p{font-size:5.5px;margin-bottom:3px;display:flex;gap:4px;align-items:flex-start}
.contact-info i{width:6px;height:6px;border-radius:50%;background:var(--orange);display:inline-block;flex:none;margin-top:1px}
.news input{display:block;width:110px;height:11px;border:none;margin-bottom:3px;font-size:5px;padding:0 3px;font-family:inherit}
.news .submit{display:inline-block;background:var(--orange);color:var(--white);font-size:5.5px;font-weight:700;padding:3px 8px}
.feature-side{margin-left:auto}
.feature-img{width:110px;height:80px;background:linear-gradient(160deg,#d9d2c8,#8b7b68)}
.footer-social{display:flex;gap:3px;justify-content:flex-end;margin-top:4px}
.footer-social span{width:8px;height:8px;background:var(--orange);display:inline-block}
.copyright{background:var(--maroon-dark);height:20px;line-height:20px;color:#cbbaba;font-size:5.5px}
</style>
</head>
<body>

<header class="topbar">
  <div class="wrap">
    <div class="brand">
      <span class="brand-mark"></span>
      <div class="brand-name">Velmora<br>Boutique Hotel</div>
    </div>
    <div class="local">
      <b>Local Information</b>
      ☀ 33 °C &nbsp;&nbsp; ◷ 08:27 am
    </div>
    <div class="live-chat">Live Chat</div>
    <div class="contact-top">
      <div class="social">Follow us &nbsp;<span></span><span></span><span></span><span></span></div>
      <div class="phone">
        <svg width="10" height="10" viewBox="0 0 24 24"><path fill="#f39a1e" d="M6.6 10.8a15 15 0 0 0 6.6 6.6l2.2-2.2c.3-.3.7-.4 1-.2 1.1.4 2.3.6 3.6.6.6 0 1 .4 1 1V20c0 .6-.4 1-1 1A17 17 0 0 1 3 4c0-.6.4-1 1-1h3.5c.6 0 1 .4 1 1 0 1.3.2 2.5.6 3.6.1.3 0 .7-.2 1z"/></svg>
        088-410-2275
      </div>
    </div>
  </div>
</header>

<nav class="nav">
  <div class="wrap">
    <ul>
      <li class="active">HOME</li>
      <li>ACCOMMODATION</li>
      <li>RESTAURANT &amp; BAR</li>
      <li>MEETINGS &amp; EVENTS</li>
      <li>BLOG</li>
      <li>SPECIAL PACKAGES</li>
      <li>CONTACT</li>
    </ul>
  </div>
</nav>

<section class="carousel">
  <div class="slide s1" role="img" aria-label="Hotel room with bed and window"></div>
  <div class="slide s2" role="img" aria-label="Warm lit bedroom interior"></div>
  <div class="slide s3" role="img" aria-label="Twin bed room with white linen"></div>
  <div class="slide s4" role="img" aria-label="Suite with double bed and lamps"></div>
  <span class="arrow l"><svg width="10" height="16" viewBox="0 0 10 16"><path d="M8 1 2 8l6 7" stroke="#fff" stroke-width="2" fill="none"/></svg></span>
  <span class="arrow r"><svg width="10" height="16" viewBox="0 0 10 16"><path d="m2 1 6 7-6 7" stroke="#fff" stroke-width="2" fill="none"/></svg></span>
</section>

<section class="booking">
  <div class="wrap">
    <div class="field"><span>Check-in</span><div class="box">dd/mm/yyyy <span>▦</span></div></div>
    <div class="field"><span>Check-out</span><div class="box">dd/mm/yyyy <span>▦</span></div></div>
    <div class="field small"><span>Rooms</span><div class="box">1 <span>▾</span></div></div>
    <div class="field small"><span>Adults</span><div class="box">1 <span>▾</span></div></div>
    <div class="field small"><span>Children</span><div class="box">0 <span>▾</span></div></div>
    <div class="field"><span>Promo code</span><div class="box">&nbsp;</div></div>
    <div class="check">
      <span class="dot"><svg width="10" height="10" viewBox="0 0 24 24"><path d="m4 12 5 5 11-11" stroke="#f39a1e" stroke-width="3" fill="none"/></svg></span>
      <span class="btn">CHECK AVAILABILITY</span>
    </div>
  </div>
</section>

<section class="welcome">
  <div class="wrap">
    <h2>Welcome to Velmora Boutique Hotel</h2>
    <p><b>Velmora Boutique</b> is a calm retreat in the green highlands of north-east Cambodia, where quiet rooms, warm service and local flavours meet. Our team will help you plan tours to lakes, waterfalls and villages nearby, arrange transfers and make each stay easy. Guests who travel far deserve rest, comfort and a place that feels like home after a long day outdoors, and <b>Velmora Boutique</b> offers just that with care in every detail.</p>
    <span class="btn-read">READ MORE</span>
  </div>
</section>

<div class="divider"></div>

<section class="facilities">
  <div class="wrap">
    <h2>FAVORITE FACILITIES</h2>
    <div class="fac-grid">
      <div class="fac">
        <svg width="22" height="22" viewBox="0 0 24 24"><path d="M6 2v9M4 2v5a2 2 0 0 0 4 0V2M6 11v11M17 2c-2 2-3 5-3 8h3v12" stroke="#e07f0c" stroke-width="1.8" fill="none"/></svg>
        <h3>SAFFRON RESTAURANT</h3>
        <p>Fresh local dishes and fine wines served in a bright room with garden views each day.</p>
        <span class="btn-read">READ MORE</span>
      </div>
      <div class="fac">
        <svg width="22" height="22" viewBox="0 0 24 24"><path d="M4 3h16l-8 9zM12 12v8M8 21h8" stroke="#e07f0c" stroke-width="1.8" fill="none"/></svg>
        <h3>AMBER BAR</h3>
        <p>Cool drinks, fresh juice and light snacks by the pool from late morning until night.</p>
        <span class="btn-read">READ MORE</span>
      </div>
      <div class="fac">
        <svg width="22" height="22" viewBox="0 0 24 24"><path d="M12 20c-5 0-9-3-9-7 3 0 6 1 9 4 3-3 6-4 9-4 0 4-4 7-9 7zM12 17c-2-3-2-7 0-11 2 4 2 8 0 11z" stroke="#e07f0c" stroke-width="1.6" fill="none"/></svg>
        <h3>SPA</h3>
        <p>Gentle massage and herbal care to relax body and mind after a day of travel.</p>
        <span class="btn-read">READ MORE</span>
      </div>
      <div class="fac">
        <svg width="22" height="22" viewBox="0 0 24 24"><path d="M3 11h18v6H3zM5 11V7h14v4M5 17v3M19 17v3" stroke="#e07f0c" stroke-width="1.8" fill="none"/></svg>
        <h3>HOTEL LOUNGE</h3>
        <p>A quiet space with soft seats, books and tea to meet friends or simply unwind.</p>
        <span class="btn-read">READ MORE</span>
      </div>
    </div>
  </div>
</section>

<section class="offers">
  <h2>OUR OFFERS</h2>
  <div class="offer-row">
    <div class="offer-img o1" role="img" aria-label="Summer sale promotional banner"></div>
    <div class="offer-info">
      <div class="pct">50% OFF</div>
      <div class="title">October Exclusive Sales</div>
      <div class="price">From: $89.00</div>
      <p><b>Booking Period:</b> from 01 Oct to 31 Oct, 2015</p>
      <p><b>Staying Period:</b> from 01 Nov to 15 Dec, 2015</p>
      <p>Save half on all deluxe rooms with free breakfast for two.</p>
      <span class="details">DETAILS</span>
    </div>
    <div class="offer-img o2" role="img" aria-label="Festival sale up to 70 percent off banner"></div>
  </div>
</section>

<section class="gallery">
  <h2>OUR GALLERY</h2>
  <div class="gal-row">
    <svg width="10" height="16" viewBox="0 0 10 16"><path d="M8 1 2 8l6 7" stroke="#999" stroke-width="2" fill="none"/></svg>
    <div class="g g1" role="img" aria-label="Bright guest room"></div>
    <div class="g g2" role="img" aria-label="Restaurant dining area"></div>
    <div class="g g3" role="img" aria-label="Hotel lobby"></div>
    <div class="g g4" role="img" aria-label="Twin room"></div>
    <div class="g g5" role="img" aria-label="Suite bedroom at night"></div>
    <svg width="10" height="16" viewBox="0 0 10 16"><path d="m2 1 6 7-6 7" stroke="#999" stroke-width="2" fill="none"/></svg>
  </div>
</section>

<footer>
  <div class="footer">
    <div class="wrap">
      <div>
        <h4>QUICK LINKS</h4>
        <div class="links">
          <span>Home</span><span>Special Packages</span>
          <span>Accomodation</span><span>Contact</span>
          <span>Restaurant &amp; Bar</span><span>Privacy Policy</span>
          <span>Meeting &amp; Events</span><span>Terms &amp; Conditions</span>
          <span>Blog</span><span>Other Services</span>
        </div>
      </div>
      <div class="contact-info">
        <h4>CONTACT INFO</h4>
        <p><i></i><span>12 Tovel Road, Orin Hill<br>Northern Province<br>Kingdom of Cambodia</span></p>
        <p><i></i>088-410-2275</p>
        <p><i></i>stay@velmorahotel.com</p>
      </div>
      <div class="news">
        <h4>GET NEWS UPDATES</h4>
        <input type="text" value="Your name">
        <input type="text" value="Your email">
        <span class="submit">SUBMIT</span>
      </div>
      <div class="feature-side">
        <div class="feature-img" role="img" aria-label="Hotel exterior with garden"></div>
        <div class="footer-social"><span></span><span></span><span></span><span></span></div>
      </div>
    </div>
  </div>
  <div class="copyright"><div class="wrap">© 2015 Velmora Boutique Hotel. All rights reserved.</div></div>
</footer>

</body>
</html>
```